Velsori Biotechnology needs a professional powerpoint design

We would like to re-design our powerpoint template(as attachment 1), it should be based on our current logo (as attachment 2). We hope the new powerpoint template could be more professional and like a biotechnology company with advanced technology.
Velsori Biotechnology is a contract development and manufacturing organization to provide high quality services to our clients in development, lead-in advanced technology and cGMP manufacturing of biopharmaceuticals from clinical to commercial manufacturing. We offers the advanced technology and services to become the best partner for clients from clinical to commercial manufacturing.
Reason: We would like to extend the deadline for this project so that designers can have more time to prepare, thanks.
Target Market(s)
Velsori Biotechnology is a contract development and manufacturing organization to provide high quality services to our clients in development, lead-in advanced technology and cGMP manufacturing of biopharmaceuticals from clinical to commercial manufacturing.
Velsori primary focus on development and manufacturing of glycoprotein pharmaceuticals against breast cancer, supplies KEP Taiwan with KEP-437 & KEP-438 for global clinical trials and commercialization in the future. Velsori offers the advanced technology and services to become the best partner for clients from clinical to commercial manufacturing.
Industry/Entity Type
Biotechnology
Requirements
Must have
- The new powerpoint design should based on our current logo.
Should not have
- The similar design with current powerpoint style. Please don't refer the design style of our current website http://www.velsori-example.com.tw/ as well, we will re-design it soon.

```html
<!DOCTYPE html>
<html lang="en">
<head>
<meta charset="utf-8">
<title>Velsori Biotechnology – Presentation Template</title>
<link href="https://fonts.googleapis.com/css2?family=Roboto:wght@300;400;500;700&display=swap" rel="stylesheet">
<style>
:root{
  --blue:#1a8ad4;
  --blue-deep:#15609f;
  --blue-soft:#5fb0e6;
  --yellow:#f6b900;
  --red:#e11c1c;
  --ink:#333a40;
  --muted:#8a9096;
  --line:#e4e7ea;
  --page:#ffffff;
  --dark:#1b1d20;
}
*{box-sizing:border-box;margin:0;padding:0}
html,body{width:1200px;height:720px;overflow:hidden;background:var(--page);font-family:'Roboto',Arial,sans-serif;color:var(--ink)}
.deck{position:relative;width:1200px;height:720px}
.slide{position:absolute;width:271px;height:152px;background:#fff;box-shadow:0 1px 3px rgba(0,0,0,.22);overflow:hidden}
.c1{left:23px}.c2{left:317px}.c3{left:613px}.c4{left:904px}
.r1{top:23px}.r2{top:199px}.r3{top:377px}.r4{top:547px}
.abs{position:absolute}
.eyebrow{position:absolute;left:12px;top:11px;font-size:6.8px;font-weight:700;color:var(--blue)}
.title{position:absolute;left:12px;top:21px;font-size:9.6px;font-weight:400;text-transform:uppercase;letter-spacing:.2px;color:var(--ink)}
.brand{position:absolute;right:9px;top:9px;display:flex;align-items:center;gap:2px;font-size:5.6px;font-weight:700;color:var(--ink);letter-spacing:.3px}
.brand i{display:block;width:4px;height:4px;background:var(--blue)}
.brand-box{position:absolute;background:#fff;border-radius:2px;display:flex;align-items:center;gap:4px;font-weight:700;color:var(--ink);letter-spacing:.5px}
.brand-box i{display:block;background:var(--blue)}
.foot{position:absolute;left:12px;right:10px;bottom:5px;display:flex;justify-content:space-between;align-items:center;font-size:3.6px;color:var(--muted)}
.foot span.pg{display:inline-block;background:#444;color:#fff;padding:1px 3px;margin-left:6px;font-size:3.6px}
.tiny{font-size:3.4px;line-height:1.35;color:#6b7177}
.photo{position:absolute}
.ph-lab{background:linear-gradient(135deg,#3b8fcf 0%,#9ccbe8 45%,#2a74b8 100%)}
.ph-scope{background:linear-gradient(120deg,#7bb3dc 0%,#2f7fc0 45%,#134f8a 100%)}
.ph-glass{background:linear-gradient(180deg,#3a86c6 0%,#1d5f9f 60%,#2d79bd 100%)}
.ph-room{background:linear-gradient(135deg,#b9d9a2 0%,#6fae6a 50%,#a9cfe0 100%)}
.ph-dark{background:radial-gradient(circle at 50% 55%,#6a4a2a 0%,#2a2320 35%,#0e0e0e 75%)}
.ph-grey{background:linear-gradient(180deg,#2a2a2a 0%,#5a5a5a 70%,#999 100%)}
.ph-person{background:radial-gradient(ellipse at 50% 60%,#4a4a4a 0%,#1a1a1a 55%,#050505 100%)}
.ph-band{background:linear-gradient(90deg,#8fb0d8 0%,#d6e3f2 35%,#5a7fd0 70%,#2f52c6 100%)}
.ph-suit{background:linear-gradient(135deg,#2b6e99 0%,#1c5a85 50%,#0f4068 100%)}
/* cover */
.cover-brand{left:129px;top:62px;width:67px;height:27px;padding-left:8px;font-size:8.5px}
.cover-brand i{width:7px;height:7px}
/* hello */
.hello h1{position:absolute;left:26px;top:14px;font-size:22px;font-weight:700;color:#fff}
.hello .sub{position:absolute;left:26px;top:45px;font-size:6.6px;color:#fff}
.hello .tiny{position:absolute;left:26px;width:128px;color:#e8f2fb}
.hello-brand{left:26px;top:97px;width:35px;height:13px;padding-left:4px;font-size:4.8px}
.hello-brand i{width:4px;height:4px}
/* quote */
.quote{position:absolute;left:0;right:0;top:62px;text-align:center;color:#fff;font-size:9.6px;letter-spacing:.2px}
.quote-by{position:absolute;left:0;right:0;top:78px;text-align:center;color:#dbeaf7;font-size:4.4px}
/* report */
.legend{position:absolute;left:58px;top:48px;font-size:3.4px;color:#666;display:flex;gap:5px}
.legend b{display:inline-block;width:4px;height:2px;margin-right:1px;vertical-align:middle}
.summary h4{position:absolute;left:152px;top:50px;font-size:5px;font-weight:500}
.summary .tiny{position:absolute;left:152px;top:57px;width:90px}
/* about */
.feat-ic{position:absolute;width:16px;height:16px;border-radius:50%;background:var(--blue);display:flex;align-items:center;justify-content:center}
.feat-h{position:absolute;font-size:5.2px;color:var(--ink)}
.feat-t{position:absolute;width:85px}
/* problem / team */
.card-img{position:absolute;top:43px;width:74px;height:49px;border-radius:3px}
.card-cap{position:absolute;top:96px;width:74px;text-align:center;font-size:5.2px}
.card-t{position:absolute;top:104px;width:74px;text-align:center}
.team-img{position:absolute;top:42px;width:74px;height:56px;border-radius:3px}
.team-n{position:absolute;top:101px;width:74px;text-align:center;font-size:5.4px}
.team-r{position:absolute;top:109px;width:74px;text-align:center;font-size:3.3px;color:#777}
/* model */
.lg-h{position:absolute;left:151px;font-size:4.8px;color:var(--blue)}
.lg-t{position:absolute;left:151px;width:100px}
/* features */
.num{position:absolute;font-size:14px;font-weight:300;color:#b9bec3}
.nt{position:absolute;font-size:4.6px;color:var(--ink)}
.nd{position:absolute;width:85px}
/* contact */
.contact-brand{left:30px;top:43px;width:44px;height:16px;padding-left:5px;font-size:5.6px}
.contact-brand i{width:4px;height:4px}
.contact h2{position:absolute;left:30px;top:67px;font-size:13px;font-weight:500;color:#fff}
.c-row{position:absolute;left:30px;display:flex;align-items:center;gap:5px;font-size:4.6px;color:#fff}
.c-row svg{width:7px;height:7px}
/* investment */
.million{position:absolute;left:0;right:0;top:86px;text-align:center;font-size:21px;font-weight:700;color:#fff;letter-spacing:.5px}
/* plan */
.plan{position:absolute;left:18px;top:48px;list-style:none}
.plan li{font-size:4.6px;color:#555;margin-bottom:9px;position:relative;padding-left:7px}
.plan li::before{content:"";position:absolute;left:0;top:1.5px;width:2px;height:2px;border-radius:50%;background:#555}
</style>
</head>
<body>
<main class="deck">

  <!-- Row 1 -->
  <section class="slide c1 r1">
    <div class="photo ph-lab" style="inset:0" role="img" aria-label="Laboratory glassware with blue liquid"></div>
    <div class="brand-box abs cover-brand"><i></i>VELSORI</div>
  </section>

  <section class="slide c2 r1 hello">
    <div class="photo ph-scope" style="inset:0" role="img" aria-label="Close-up of a laboratory microscope"></div>
    <h1>Hello!</h1>
    <p class="sub">Welcome to the Presentation</p>
    <p class="tiny" style="top:56px">Lorem ipsum dolor sit amet, consectetur adipiscing elit, sed do eiusmod tempor.</p>
    <p class="tiny" style="top:74px">Lorem ipsum dolor sit amet, consectetur adipiscing elit.</p>
    <div class="brand-box abs hello-brand"><i></i>VELSORI</div>
  </section>

  <section class="slide c3 r1">
    <div class="photo ph-glass" style="inset:0" role="img" aria-label="Laboratory apparatus with flask and tubing"></div>
    <p class="quote">“LIFE IS ALL ABOUT HAPPINESS”</p>
    <p class="quote-by">- Marcus Delane</p>
  </section>

  <section class="slide c4 r1">
    <p class="eyebrow">The Report</p>
    <h2 class="title">Here’s our research report</h2>
    <div class="brand"><i></i>VELSORI</div>
    <div class="legend"><span><b style="background:var(--blue)"></b>Users</span><span><b style="background:var(--yellow)"></b>Clients</span></div>
    <svg class="abs" style="left:20px;top:58px" width="130" height="72" viewBox="0 0 130 72">
      <g font-size="3" fill="#fff" text-anchor="middle" font-family="Roboto,sans-serif">
        <rect x="9" y="8" width="9" height="55" fill="#1a8ad4"/><text x="13.5" y="12">3.1</text>
        <rect x="19" y="20" width="9" height="43" fill="#f6b900"/><text x="23.5" y="24">2.4</text>
        <rect x="40" y="19" width="9" height="44" fill="#1a8ad4"/><text x="44.5" y="23">2.5</text>
        <rect x="50" y="45" width="9" height="18" fill="#f6b900"/><text x="54.5" y="49">1</text>
        <rect x="71" y="30" width="9" height="33" fill="#1a8ad4"/><text x="75.5" y="34">1.9</text>
        <rect x="81" y="14" width="9" height="49" fill="#f6b900"/><text x="85.5" y="18">2.8</text>
        <rect x="102" y="42" width="9" height="21" fill="#1a8ad4"/><text x="106.5" y="46">1.2</text>
        <rect x="112" y="36" width="9" height="27" fill="#f6b900"/><text x="116.5" y="40">1.5</text>
      </g>
      <line x1="4" y1="63" x2="126" y2="63" stroke="#ddd" stroke-width=".5"/>
      <g font-size="3" fill="#777" text-anchor="middle" font-family="Roboto,sans-serif">
        <text x="18.5" y="68">2013</text><text x="49.5" y="68">2014</text><text x="80.5" y="68">2015</text><text x="111.5" y="68">2017</text>
      </g>
    </svg>
    <div class="summary">
      <h4>The Summary</h4>
      <p class="tiny">Lorem ipsum dolor sit amet, consectetur adipiscing elit, sed do eiusmod tempor incididunt ut labore et dolore magna aliqua. Ut enim ad minim veniam, quis nostrud exercitation ullamco laboris.</p>
    </div>
    <div class="foot"><span>Velsori Biotech</span><span>velsoribiotech.com<span class="pg">13</span></span></div>
  </section>

  <!-- Row 2 -->
  <section class="slide c1 r2">
    <p class="eyebrow">About Us</p>
    <h2 class="title">We are here for peace</h2>
    <div class="brand"><i></i>VELSORI</div>
    <div class="photo ph-room" style="left:12px;top:42px;width:122px;height:66px;border-radius:2px" role="img" aria-label="Modern operating room"></div>
    <div class="feat-ic" style="left:145px;top:52px"><svg width="8" height="8" viewBox="0 0 8 8"><rect x="1" y="1.5" width="6" height="5" fill="none" stroke="#fff" stroke-width=".8"/><line x1="2" y1="3.5" x2="6" y2="3.5" stroke="#fff" stroke-width=".7"/></svg></div>
    <p class="feat-h" style="left:170px;top:49px">Inner Development</p>
    <p class="feat-t tiny" style="left:170px;top:56px">Lorem ipsum dolor sit amet, consectetur adipiscing elit.</p>
    <div class="feat-ic" style="left:145px;top:79px"><svg width="8" height="8" viewBox="0 0 8 8"><circle cx="4" cy="4" r="2.6" fill="none" stroke="#fff" stroke-width=".8"/><circle cx="4" cy="4" r=".9" fill="#fff"/></svg></div>
    <p class="feat-h" style="left:170px;top:77px">We Believe</p>
    <p class="feat-t tiny" style="left:170px;top:84px">Lorem ipsum dolor sit amet, consectetur adipiscing elit.</p>
    <div class="feat-ic" style="left:145px;top:106px"><svg width="8" height="8" viewBox="0 0 8 8"><line x1="1.5" y1="6.5" x2="5.5" y2="2.5" stroke="#fff" stroke-width="1"/><circle cx="5.8" cy="2.2" r="1.3" fill="none" stroke="#fff" stroke-width=".7"/></svg></div>
    <p class="feat-h" style="left:170px;top:105px">We Repair</p>
    <p class="feat-t tiny" style="left:170px;top:112px">Lorem ipsum dolor sit amet, consectetur adipiscing elit.</p>
    <div class="foot"><span>Velsori Biotech</span><span>velsoribiotech.com<span class="pg">04</span></span></div>
  </section>

  <section class="slide c2 r2">
    <p class="eyebrow">Our Vission</p>
    <h2 class="title">We have a dream</h2>
    <div class="brand"><i></i>VELSORI</div>
    <p class="tiny abs" style="left:12px;top:41px;width:248px">Lorem ipsum dolor sit amet, consectetur adipiscing elit. <b style="color:var(--blue)">Aenean commodo</b> ligula eget dolor. Aenean massa. Cum sociis natoque penatibus et magnis dis parturient montes, nascetur ridiculus mus. Donec quam felis, ultricies nec, pellentesque eu, pretium quis, sem nulla consequat massa quis enim donec pede justo.</p>
    <p class="tiny abs" style="left:12px;top:66px;width:248px">Nam quam nunc, blandit vel, luctus pulvinar, hendrerit id, lorem. Maecenas nec odio et ante <b style="color:var(--blue)">tincidunt tempus</b>. Donec vitae sapien ut libero venenatis faucibus. Nullam quis ante. Etiam sit amet orci eget eros faucibus tincidunt. Duis leo. Sed fringilla mauris sit amet nibh donec sodales.</p>
    <p class="tiny abs" style="left:12px;top:91px;width:248px">Cum sociis natoque penatibus et magnis dis parturient <b style="color:var(--blue)">montes</b>, nascetur ridiculus mus. Donec quam felis, ultricies nec, pellentesque eu, pretium quis, sem. Nulla consequat massa quis enim. Donec pede justo, fringilla vel, aliquet nec, vulputate eget, arcu. In enim justo, rhoncus ut, imperdiet a, venenatis vitae.</p>
    <div class="foot"><span>Velsori Biotech</span><span>velsoribiotech.com<span class="pg">05</span></span></div>
  </section>

  <section class="slide c3 r2">
    <p class="eyebrow">The Common Problem</p>
    <h2 class="title">People want more to be happy</h2>
    <div class="brand"><i></i>VELSORI</div>
    <div class="card-img ph-dark" style="left:12px" role="img" aria-label="Hand holding a lit match in darkness"></div>
    <div class="card-img ph-dark" style="left:99px" role="img" aria-label="Glasses of whisky on a dark table"></div>
    <div class="card-img ph-grey" style="left:186px" role="img" aria-label="Misty mountain ridge"></div>
    <p class="card-cap" style="left:12px">Main</p>
    <p class="card-cap" style="left:99px">Partial</p>
    <p class="card-cap" style="left:186px">Overall</p>
    <p class="card-t tiny" style="left:12px">Lorem ipsum dolor sit amet, consectetur adipiscing elit, sed do.</p>
    <p class="card-t tiny" style="left:99px">Lorem ipsum dolor sit amet, consectetur adipiscing elit, sed do.</p>
    <p class="card-t tiny" style="left:186px">Lorem ipsum dolor sit amet, consectetur adipiscing elit, sed do.</p>
    <div class="foot"><span>Velsori Biotech</span><span>velsoribiotech.com<span class="pg">06</span></span></div>
  </section>

  <section class="slide c4 r2">
    <p class="eyebrow">Team</p>
    <h2 class="title">Our members</h2>
    <div class="brand"><i></i>VELSORI</div>
    <div class="team-img ph-person" style="left:12px" role="img" aria-label="Portrait of a team member"></div>
    <div class="team-img ph-person" style="left:99px" role="img" aria-label="Portrait of a team member"></div>
    <div class="team-img ph-person" style="left:186px" role="img" aria-label="Portrait of a team member"></div>
    <p class="team-n" style="left:12px">Owen Tarrick</p>
    <p class="team-n" style="left:99px">Lina Corvell</p>
    <p class="team-n" style="left:186px">Dario Fennick</p>
    <p class="team-r" style="left:12px">CEO, Founder</p>
    <p class="team-r" style="left:99px">CTO, Founder</p>
    <p class="team-r" style="left:186px">Marketing Manager</p>
    <div class="foot"><span>Velsori Biotech</span><span>velsoribiotech.com<span class="pg">14</span></span></div>
  </section>

  <!-- Row 3 -->
  <section class="slide c1 r3">
    <p class="eyebrow">Our Solution</p>
    <h2 class="title">We have a solution</h2>
    <div class="brand"><i></i>VELSORI</div>
    <div class="photo ph-band" style="left:12px;top:42px;width:248px;height:50px;border-radius:2px" role="img" aria-label="Row of laboratory test tubes"></div>
    <p class="abs" style="left:0;right:0;top:96px;text-align:center;font-size:5.8px">How To Achieve It!</p>
    <p class="tiny abs" style="left:12px;top:105px;width:248px;text-align:center">Lorem ipsum dolor sit amet, consectetur adipiscing elit, sed do eiusmod tempor incididunt ut labore et dolore magna aliqua. Ut enim ad minim veniam, quis nostrud exercitation ullamco laboris nisi ut aliquip ex ea commodo consequat. Duis aute irure dolor in reprehenderit.</p>
    <div class="foot"><span>Velsori Biotech</span><span>velsoribiotech.com<span class="pg">07</span></span></div>
  </section>

  <section class="slide c2 r3">
    <p class="eyebrow">The Project Model</p>
    <h2 class="title">Here’s why invest on this solution</h2>
    <div class="brand"><i></i>VELSORI</div>
    <svg class="abs" style="left:40px;top:42px" width="76" height="76" viewBox="-38 -38 76 76">
      <path d="M0 0 L0 -34 A34 34 0 0 1 34 0 Z" fill="#f6b900"/>
      <path d="M0 0 L34 0 A34 34 0 0 1 24.8 23.3 Z" fill="#e11c1c"/>
      <path d="M0 0 L24.8 23.3 A34 34 0 1 1 0 -34 Z" fill="#1a8ad4"/>
      <g font-family="Roboto,sans-serif" font-size="5.5" font-weight="700" fill="#fff" text-anchor="middle">
        <text x="14" y="-10">25%</text><text x="21" y="9">12%</text><text x="-14" y="3">63%</text>
      </g>
    </svg>
    <p class="abs" style="left:38px;top:122px;font-size:4.2px">Business Revenue Share Diagram</p>
    <p class="lg-h" style="top:50px">67% For Church</p>
    <p class="lg-t tiny" style="top:57px">Lorem ipsum dolor sit amet, consectetur adipiscing elit, sed do eiusmod tempor.</p>
    <p class="lg-h" style="top:78px">25% For Clients</p>
    <p class="lg-t tiny" style="top:85px">Lorem ipsum dolor sit amet, consectetur adipiscing elit, sed do eiusmod tempor.</p>
    <p class="lg-h" style="top:106px">12% For Users</p>
    <p class="lg-t tiny" style="top:113px">Lorem ipsum dolor sit amet, consectetur adipiscing elit, sed do eiusmod tempor.</p>
    <div class="foot"><span>Velsori Biotech</span><span>velsoribiotech.com<span class="pg">08</span></span></div>
  </section>

  <section class="slide c3 r3">
    <p class="eyebrow">Top Features</p>
    <h2 class="title">We are different</h2>
    <div class="brand"><i></i>VELSORI</div>
    <p class="num" style="left:12px;top:50px">01</p><p class="nt" style="left:39px;top:50px">Your Title Here</p><p class="nd tiny" style="left:39px;top:57px">Lorem ipsum dolor sit amet, consectetur adipiscing elit, sed do.</p>
    <p class="num" style="left:12px;top:77px">02</p><p class="nt" style="left:39px;top:77px">Your Title Here</p><p class="nd tiny" style="left:39px;top:84px">Lorem ipsum dolor sit amet, consectetur adipiscing elit, sed do.</p>
    <p class="num" style="left:12px;top:104px">03</p><p class="nt" style="left:39px;top:104px">Your Title Here</p><p class="nd tiny" style="left:39px;top:111px">Lorem ipsum dolor sit amet, consectetur adipiscing elit, sed do.</p>
    <p class="num" style="left:144px;top:50px">04</p><p class="nt" style="left:171px;top:50px">Your Title Here</p><p class="nd tiny" style="left:171px;top:57px">Lorem ipsum dolor sit amet, consectetur adipiscing elit, sed do.</p>
    <p class="num" style="left:144px;top:77px">05</p><p class="nt" style="left:171px;top:77px">Your Title Here</p><p class="nd tiny" style="left:171px;top:84px">Lorem ipsum dolor sit amet, consectetur adipiscing elit, sed do.</p>
    <p class="num" style="left:144px;top:104px">06</p><p class="nt" style="left:171px;top:104px">Your Title Here</p><p class="nd tiny" style="left:171px;top:111px">Lorem ipsum dolor sit amet, consectetur adipiscing elit, sed do.</p>
    <div class="foot"><span>Velsori Biotech</span><span>velsoribiotech.com<span class="pg">09</span></span></div>
  </section>

  <section class="slide c4 r3 contact">
    <div class="photo ph-suit" style="inset:0" role="img" aria-label="Businessman adjusting his suit, blue toned"></div>
    <div class="brand-box abs contact-brand"><i></i>VELSORI</div>
    <h2>Contact Us</h2>
    <p class="c-row" style="top:88px"><svg viewBox="0 0 8 8"><path d="M2 1 L3.2 2.6 L2.5 3.4 Q3.5 5 4.8 5.6 L5.6 4.8 L7 6 L6 7.2 Q2.5 6.5 0.9 2 Z" fill="#fff"/></svg>+6640182736</p>
    <p class="c-row" style="top:101px"><svg viewBox="0 0 8 8"><rect x="1" y="2" width="6" height="4.2" fill="none" stroke="#fff" stroke-width=".7"/><path d="M1 2 L4 4.4 L7 2" fill="none" stroke="#fff" stroke-width=".7"/></svg>hello@velsorimail.com</p>
    <p class="c-row" style="top:114px"><svg viewBox="0 0 8 8"><circle cx="4" cy="4" r="3" fill="none" stroke="#fff" stroke-width=".7"/><line x1="1" y1="4" x2="7" y2="4" stroke="#fff" stroke-width=".6"/></svg>www.velsori-example.com</p>
  </section>

  <!-- Row 4 -->
  <section class="slide c1 r4">
    <p class="eyebrow">Our Portfolio</p>
    <h2 class="title">Here’s a few sample</h2>
    <div class="brand"><i></i>VELSORI</div>
    <div class="photo ph-grey" style="left:12px;top:42px;width:74px;height:33px" role="img" aria-label="Misty mountain ridge"></div>
    <div class="photo ph-scope" style="left:88px;top:42px;width:47px;height:55px" role="img" aria-label="Microscope eyepieces"></div>
    <div class="photo ph-dark" style="left:137px;top:42px;width:49px;height:55px" role="img" aria-label="Glasses of whisky"></div>
    <div class="photo ph-grey" style="left:188px;top:42px;width:72px;height:33px" role="img" aria-label="Person writing at a desk"></div>
    <div class="photo ph-glass" style="left:12px;top:77px;width:74px;height:57px" role="img" aria-label="Laboratory flask apparatus"></div>
    <div class="photo ph-dark" style="left:88px;top:99px;width:98px;height:35px" role="img" aria-label="Lit match in darkness"></div>
    <div class="photo ph-lab" style="left:188px;top:77px;width:72px;height:57px" role="img" aria-label="Laboratory bottles and glassware"></div>
    <div class="foot"><span>Velsori Biotech</span><span>velsoribiotech.com<span class="pg">10</span></span></div>
  </section>

  <section class="slide c2 r4">
    <p class="eyebrow">Investment Needed</p>
    <h2 class="title">We need...</h2>
    <div class="brand"><i></i>VELSORI</div>
    <div class="photo ph-scope" style="left:0;right:0;top:42px;height:87px" role="img" aria-label="Microscope lens, blue toned"></div>
    <p class="million" style="top:72px">$1 MILLION</p>
    <div class="foot"><span>Velsori Biotech</span><span>velsoribiotech.com<span class="pg">11</span></span></div>
  </section>

  <section class="slide c3 r4">
    <p class="eyebrow">Our Plan</p>
    <h2 class="title">How the money will spent</h2>
    <div class="brand"><i></i>VELSORI</div>
    <ul class="plan" style="top:44px">
      <li>Lorem Ipsum has been the industry's standard dummy text ever since.</li>
      <li>Lorem Ipsum has been the text ever since.</li>
      <li>Lorem Ipsum has been the industry's standard dummy text ever since.</li>
      <li>Lorem Ipsum been the industry's standard dummy text ever since.</li>
      <li>Lorem Ipsum has been the industry's standard dummy text ever since.</li>
      <li>Lorem Ipsum has been standard dummy text ever since.</li>
      <li>Lorem Ipsum has been the industry's stadummy text ever since.</li>
    </ul>
    <div class="foot"><span>Velsori Biotech</span><span>velsoribiotech.com<span class="pg">12</span></span></div>
  </section>

</main>
</body>
</html>
```